Professional Services/Construction Management (Millwork) Biz Cards

We've decided on a logo and have our color palette set, now we want to design some very professional looking cards that make a strong first impression - they'll reflect our tagline (that we're going to put on the back: Innovative. Professional. Leaders.

The example business card shows generally the direction we've been thinking of going for the back side - **but we're open to other ideas**

Target Market(s)

The cards should target more high-end (wealthy) owners and general contracting companies. We want them to convey a strong first impression - in a professional and not garish way.

Industry/Entity Type

Construction Company

Contact Information for Business Card

There needs to be a place for our company contractor's license number and business address. We want to also have people's names, titles, phone number, email address. The back can be the logo, tagline and web address

Requirements
Must have
• follow our color palette
Nice to have
• Font & Styles should compliment the Harbor Joinery fonts, but not necessarily match exactly

```html
<!DOCTYPE html>
<html lang="en">
<head>
<meta charset="utf-8">
<title>Harbor Joinery – Business Cards</title>
<link rel="stylesheet" href="https://fonts.googleapis.com/css2?family=Open+Sans:wght@400;600;700&display=swap">
<style>
  :root {
    --backdrop: #2b2e33;
    --navy: #1c2c5e;
    --navy-text: #1f2d5c;
    --paper: #ffffff;
    --ink: #1a1a1a;
    --brown: #5a4e44;
  }
  * { box-sizing: border-box; margin: 0; padding: 0; }
  html, body {
    width: 1200px;
    height: 864px;
    overflow: hidden;
    background: var(--backdrop);
    font-family: "Open Sans", Arial, sans-serif;
  }
  .sheet {
    position: relative;
    width: 1200px;
    height: 864px;
  }
  .card {
    position: absolute;
    left: 320px;
    width: 560px;
    height: 320px;
    border-radius: 4px;
    overflow: hidden;
  }
  /* Card back: brand face */
  .card--back {
    top: 72px;
    background: var(--navy);
    display: flex;
    align-items: center;
    justify-content: center;
  }
  .brand-wordmark {
    color: var(--paper);
    font-weight: 700;
    font-size: 46px;
    letter-spacing: 1px;
    margin-top: 90px;
  }
  /* Card front: contact face */
  .card--front {
    top: 472px;
    background: var(--paper);
  }
  .person {
    position: absolute;
    left: 34px;
    top: 132px;
  }
  .person__name {
    color: var(--navy-text);
    font-weight: 700;
    font-size: 19px;
    line-height: 1.1;
  }
  .person__title {
    color: var(--ink);
    font-size: 13px;
  }
  .badge {
    position: absolute;
    right: 30px;
    top: 34px;
    display: flex;
    align-items: center;
    gap: 10px;
  }
  .badge__dot {
    width: 26px;
    height: 26px;
    border-radius: 50%;
    background: var(--navy);
  }
  .badge__name {
    color: var(--navy-text);
    font-weight: 700;
    font-size: 20px;
  }
  .contact {
    position: absolute;
    right: 30px;
    bottom: 26px;
    text-align: right;
    color: var(--ink);
    font-size: 14px;
    line-height: 1.6;
  }
  .contact__line {
    display: flex;
    justify-content: flex-end;
    align-items: center;
    gap: 8px;
  }
  .contact__icon { width: 12px; height: 12px; fill: var(--navy); }
  .contact__label { color: var(--navy-text); font-weight: 700; }
</style>
</head>
<body>
<main class="sheet">
  <section class="card card--back" aria-label="Card back">
    <div class="brand-wordmark">Harbor Joinery</div>
  </section>

  <section class="card card--front" aria-label="Card front">
    <div class="badge">
      <span class="badge__dot"></span>
      <span class="badge__name">Harbor Joinery</span>
    </div>

    <div class="person">
      <div class="person__name">Daniel Reeves</div>
      <div class="person__title">Managing Director</div>
    </div>

    <div class="contact">
      <div class="contact__line">
        <span>(044)-555-0182</span>
        <svg class="contact__icon" viewBox="0 0 24 24" aria-hidden="true"><path d="M6.6 10.8a15 15 0 0 0 6.6 6.6l2.2-2.2a1 1 0 0 1 1-.25 11.4 11.4 0 0 0 3.6.57 1 1 0 0 1 1 1V20a1 1 0 0 1-1 1A17 17 0 0 1 3 4a1 1 0 0 1 1-1h3.5a1 1 0 0 1 1 1c0 1.25.2 2.45.57 3.6a1 1 0 0 1-.25 1z"/></svg>
      </div>
      <div class="contact__line">
        <span>info@harborjoinery.com</span>
        <svg class="contact__icon" viewBox="0 0 24 24" aria-hidden="true"><path d="M2 5h20v14H2z M3 6l9 7 9-7" fill="none" stroke="#1c2c5e" stroke-width="2"/></svg>
      </div>
      <div class="contact__line">
        <span><span class="contact__label">Lic Number:</span> 87654321</span>
      </div>
      <div class="contact__line">
        <span>48 Quayside Lane, Portsmouth, Hampshire, 204815</span>
      </div>
    </div>
  </section>
</main>
</body>
</html>
```